Lawn Sign For Construction Projects - Brisk Current

This contest is for a lawn sign that will be placed in the front yard of recently completed construction projects. The goal here is to have a bold advertising sign that is visible from a vehicle driving past.

We are still deciding on the default size for our sign, we also may use multiple sizes. The two sizes we will more than likely be using are: 18"h x 24"w and 24"h x 36"w.

Preference will be given to designers that submit original designs that tie into our current brand and are either in both the size formats listed above or are easy to scale in photoshop or illustrator.

In the files, you will see our logo and an example of a lawn sign.

Please contact us with any questions or comments you may have!

Thank You,
- The Brisk Current Team

Industry/Entity Type

Residential Construction

Colors
34a7d8
ffffff
faa54b

Requirements
Nice to have
• 1. The sign must tie into our current branding and color scheme.
• 2. The sign must be clearly visible and readable.
• 3. The sign must include our phone number in readable print.
• 4. Our website written in small print along the bottom of the sign.
• 5. Must mention we install the following products:
• a.) Solar
• b.) Roofing
• c.) Windows
• d.) Artificial Lawn
• e.) Whole House Fans
• f.) Patio Covers

```html
<!DOCTYPE html>
<html lang="en">
<head>
<meta charset="utf-8">
<title>Brisk Current – Lawn Sign</title>
<link rel="stylesheet" href="https://fonts.googleapis.com/css2?family=Montserrat:wght@500;600;700;800&family=Exo+2:wght@700&display=swap">
<style>
  :root {
    --brand-blue: #1f80c8;
    --sky-blue: #34a7d8;
    --deep-blue: #1a62b0;
    --navy: #173a6a;
    --orange: #faa54b;
    --leaf-green: #8db04c;
    --grass-green: #6fb52c;
    --white: #ffffff;
    --glow: #bfe3f5;
  }
  html, body {
    margin: 0;
    padding: 0;
    overflow: hidden;
    background: var(--white);
  }
  .sign {
    position: relative;
    width: 1200px;
    height: 900px;
    overflow: hidden;
    background: var(--white);
    font-family: "Montserrat", Arial, sans-serif;
  }
  .mosaic-backdrop {
    position: absolute;
    inset: 0 0 250px 0;
    background:
      linear-gradient(100deg,
        #1f7fd0 0%, #2f9be0 22%, #48b8e6 38%,
        #9cc98a 58%, #8db04c 78%, #a9c878 100%);
    -webkit-mask-image: linear-gradient(180deg, #000 0%, rgba(0,0,0,.75) 40%, rgba(0,0,0,0) 100%);
            mask-image: linear-gradient(180deg, #000 0%, rgba(0,0,0,.75) 40%, rgba(0,0,0,0) 100%);
  }
  .web-strip {
    position: absolute;
    left: 0;
    top: 0;
  }
  .web-address {
    position: absolute;
    left: 38px;
    top: 250px;
    transform: translate(-50%, -50%) rotate(-90deg);
    color: var(--white);
    font-weight: 700;
    font-size: 24px;
    letter-spacing: 3px;
    white-space: nowrap;
  }
  .brand-mark {
    position: absolute;
    left: 530px;
    top: 215px;
    width: 140px;
    height: 140px;
    border-radius: 50%;
    border: 14px solid var(--orange);
    box-sizing: border-box;
  }
  .brand-name {
    position: absolute;
    left: 0;
    right: 0;
    top: 362px;
    margin: 0;
    text-align: center;
    color: var(--brand-blue);
    font-weight: 700;
    font-size: 80px;
    line-height: 1;
    letter-spacing: 1px;
    white-space: nowrap;
  }
  .phone {
    position: absolute;
    left: 0;
    right: 0;
    top: 458px;
    margin: 0;
    text-align: center;
    color: var(--deep-blue);
    font-family: "Exo 2", Arial, sans-serif;
    font-weight: 700;
    font-size: 54px;
    letter-spacing: 3px;
    white-space: nowrap;
  }
  .install-band {
    position: absolute;
    left: 0;
    top: 560px;
  }
  .install-copy {
    position: absolute;
    left: 34px;
    top: 592px;
    width: 1160px;
    transform: rotate(4.4deg);
    transform-origin: left top;
  }
  .install-title {
    margin: 0;
    color: var(--brand-blue);
    font-weight: 800;
    font-size: 42px;
    line-height: 1.1;
    letter-spacing: 1px;
    white-space: nowrap;
  }
  .install-list {
    margin: 14px 0 0 4px;
    padding: 0;
    list-style: none;
    display: flex;
    flex-wrap: nowrap;
    color: var(--deep-blue);
    font-weight: 600;
    font-size: 23px;
    line-height: 1.2;
  }
  .install-list li {
    flex: 0 0 auto;
    white-space: nowrap;
  }
  .install-list li + li::before {
    content: "|";
    margin: 0 14px;
  }
  .grass-edge {
    position: absolute;
    left: 0;
    right: 0;
    bottom: 0;
    height: 120px;
    background: linear-gradient(180deg, rgba(111,181,44,0) 0%, #8fcc4a 35%, var(--grass-green) 70%, #4f9a1e 100%);
  }
</style>
</head>
<body>
<main class="sign">
  <div class="mosaic-backdrop" role="img" aria-label="Mosaic of blue and green triangles fading into white"></div>

  <svg class="web-strip" width="90" height="640" viewBox="0 0 90 640" aria-hidden="true">
    <polygon points="0,0 78,0 78,560 0,630" fill="var(--orange)"/>
  </svg>
  <div class="web-address">WWW.BRISKCURRENT.COM</div>

  <div class="brand-mark" aria-hidden="true"></div>
  <h1 class="brand-name">BRISK CURRENT</h1>
  <p class="phone">0800-555-0192</p>

  <svg class="install-band" width="1200" height="340" viewBox="0 0 1200 340" aria-hidden="true">
    <defs>
      <linearGradient id="bandGlow" x1="0" y1="0" x2="0" y2="1">
        <stop offset="0" stop-color="var(--glow)"/>
        <stop offset="1" stop-color="var(--white)"/>
      </linearGradient>
    </defs>
    <polygon points="0,20 1200,140 1200,340 0,340" fill="var(--white)"/>
    <polygon points="0,20 1200,140 1200,172 0,52" fill="url(#bandGlow)"/>
  </svg>

  <section class="install-copy">
    <h2 class="install-title">WE INSTALL:</h2>
    <ul class="install-list">
      <li>Solar</li>
      <li>Roofing</li>
      <li>Windows</li>
      <li>Artificial Lawn</li>
      <li>Whole House Fans</li>
      <li>Patio Covers</li>
    </ul>
  </section>

  <div class="grass-edge" role="img" aria-label="Strip of green lawn grass along the bottom edge"></div>
</main>
</body>
</html>
```